Below Par Parenting

I would like a poster (size to be agreed) created for the wording that I have composed and which I have pasted below. The poster is for my own personal gratification. It is not for commercial use. The message is driven by honesty and a profound sense of mea culpa. I am open to ideas regarding style and presentation.
I am an awful parent. No question. I am not cut out for this shit. I’m too quick to temper. I turn everything into a test of wills. I’m not down for food on the floor, for having my car trashed with your stink and detritus, for having the walls of my house daubed in your greasy fingerprints. I want to listen to The Marrows not Up the Paper Ladder on repeat. I enjoyed making you but, on reflection, I should have pulled out. Let me go back in time to that great waste of space and energy that is ante-natal classes and tell that boho with the flowery dress and curly hair, ‘Why are you concentrating on the first five seconds? All the pain comes later. Why aren’t you telling us what to do when they won’t sleep, when they won’t sit in their high chairs, when they won’t sleep on the aeroplane?’ Boy, I wish I could play it loosey-goosey like those left-leaning parents I see going ‘coo-coo’ in Benvolti’s but I’m not built like that. I am a right-wing despot. It’s Nazi Germany back at my place. I’m not interested in your meltdowns and tantrums. You want to writhe on the floor in the car park going red in the face? Make my day. You want to go spastic because I won’t let you watch TV for five hours straight? I don’t give a shit. Read my lips. I won’t pander to it. My wife says you’re babies but all I see is little people with an agenda. I’ve got naughty steps and sin-bins all over the joint. I wish I wasn’t the tyrant, the Valdarrez and the Okoro Tembe I am but it is what it is. I blame my parents and they, in turn, will blame me and their parents. Understand I don’t want to infect you too much with my bad behavior but if you could stop making such a scene in public places with your screaming, your bitching and your all round refusal to play nice then maybe, just maybe, we’d have a chance and I wouldn’t be such an awful parent.

```html
<!DOCTYPE html>
<html lang="en">
<head>
<meta charset="utf-8">
<title>Below Par Parenting</title>
<link rel="stylesheet" href="https://fonts.googleapis.com/css2?family=Ubuntu:wght@400&display=swap">
<style>
  :root {
    --frame: #eef3ee;
    --sky-deep: #2f6f86;
    --sky-mid: #6fb3bf;
    --glow: #f7fbf2;
    --meadow: #d9e27a;
    --meadow-deep: #9fc25c;
    --ink: #34495a;
    --ink-shadow: rgba(255, 255, 255, 0.55);
  }
  html, body {
    margin: 0;
    padding: 0;
    overflow: hidden;
    background: var(--frame);
  }
  .poster {
    position: relative;
    width: 848px;
    height: 1200px;
    background: var(--frame);
    overflow: hidden;
    font-family: "Ubuntu", sans-serif;
    color: var(--ink);
  }
  .sky {
    position: absolute;
    left: 12px;
    top: 12px;
    width: 824px;
    height: 1176px;
    background:
      radial-gradient(ellipse 55% 45% at 50% 55%, var(--glow) 0%, rgba(247,251,242,0.85) 30%, rgba(247,251,242,0) 75%),
      linear-gradient(180deg, var(--sky-deep) 0%, var(--sky-mid) 30%, #bfe0d6 52%, var(--meadow) 78%, var(--meadow-deep) 100%);
  }
  .poem {
    position: absolute;
    inset: 0;
    margin: 0;
  }
  .line {
    position: absolute;
    left: var(--x);
    top: var(--y);
    transform: translateY(-50%);
    margin: 0;
    white-space: nowrap;
    font-size: 17px;
    line-height: 1;
    text-shadow: 0 1px 2px var(--ink-shadow);
  }
  .m { font-size: 22px; }
  .l { font-size: 25px; }
  .xl { font-size: 28px; }
  .line .small { font-size: 17px; }
</style>
</head>
<body>
<div class="poster">
  <div class="sky" role="img" aria-label="Bright sky with sunlight rays bursting from the centre, teal clouds above and yellow-green light below"></div>
  <div class="poem">
    <p class="line xl" style="--x:143px;--y:30px">I am an awful parent.<span class="small"> No question.</span></p>
    <p class="line" style="--x:145px;--y:64px">I am not cut out for this shit. I’m too quick to temper.</p>
    <p class="line l" style="--x:147px;--y:93px">too ready to go Nagasaki.</p>
    <p class="line" style="--x:182px;--y:120px">I’m not down for food on the floor, for having my car smeared</p>
    <p class="line" style="--x:209px;--y:147px">with your stink and detritus, for having the walls</p>
    <p class="line l" style="--x:232px;--y:175px"><span class="small">of my house daubed in your bolognaise </span>fingerprints.</p>
    <p class="line" style="--x:112px;--y:202px">I want to listen to The Marrows not Up the Paper Ladder on repeat.</p>
    <p class="line m" style="--x:147px;--y:230px">I enjoyed making you but, on reflection,</p>
    <p class="line l" style="--x:154px;--y:263px">I should have pulled out.</p>
    <p class="line" style="--x:162px;--y:298px">Let me go back in time to that great waste of space and energy that was</p>
    <p class="line" style="--x:115px;--y:325px">ante-natal classes and tell that boho with the flowery dress,</p>
    <p class="line m" style="--x:120px;--y:356px">‘Why are you concentrating on the labour?</p>
    <p class="line m" style="--x:277px;--y:387px">All the hard work comes later.</p>
    <p class="line m" style="--x:108px;--y:420px">‘Boy, I wish I could play it loosey-goosey<span class="small"> like those left-leaning parents</span></p>
    <p class="line" style="--x:160px;--y:452px">I see going ‘coo-coo’ in Benvolti’s but I’m not built like that.</p>
    <p class="line l" style="--x:153px;--y:485px">I am a right-wing despot.</p>
    <p class="line" style="--x:117px;--y:518px">It’s Guantanamo Bay back at my place with a sin bin here and a naughty step there.</p>
    <p class="line m" style="--x:148px;--y:549px">I’m not interested in your meltdowns and tantrums.</p>
    <p class="line" style="--x:141px;--y:582px">You want to writhe on the floor in the car park going red in the face?</p>
    <p class="line m" style="--x:365px;--y:613px">Make my day.</p>
    <p class="line" style="--x:180px;--y:643px">You want to go spastic because I won’t let you watch TV</p>
    <p class="line" style="--x:368px;--y:672px">for five hours straight?</p>
    <p class="line l" style="--x:118px;--y:705px">I don’t give a shit.<span class="small"> Read my lips. </span>I won’t pander to it.</p>
    <p class="line" style="--x:200px;--y:741px">My wife says you’re babies but all I see is little people with</p>
    <p class="line" style="--x:241px;--y:767px">an agenda and their own language.</p>
    <p class="line m" style="--x:215px;--y:799px">What is it that you speak?<span class="small"> Hutu with Hebrew?</span></p>
    <p class="line" style="--x:166px;--y:829px">I’ve got naughty steps and sin-bins all over the joint.</p>
    <p class="line m" style="--x:156px;--y:860px">Damn, I wish I wasn’t the tyrant,<span class="small"> the Valdarrez</span></p>
    <p class="line" style="--x:203px;--y:889px">and the Okoro Tembe I am but it is what it is.</p>
    <p class="line m" style="--x:155px;--y:922px"><span class="small">But who am I kidding? </span>You don’t respect me or my mortgage.</p>
    <p class="line" style="--x:180px;--y:953px">I can’t pooh in the bath like you do (I pee but that’s not the same).</p>
    <p class="line" style="--x:232px;--y:983px">You’re up with there with Ricky Vane leaving your bedroom</p>
    <p class="line l" style="--x:247px;--y:1014px">looking like the Tet Offensive.</p>
    <p class="line m" style="--x:205px;--y:1050px"><span class="small">I give up. </span>I sue for peace.<span class="small"> Hollingworth style.</span></p>
    <p class="line m" style="--x:208px;--y:1082px"><span class="small">I’ll be downstairs beaten with a whisky. </span>Do as you please.</p>
    <p class="line m" style="--x:313px;--y:1112px"><span class="small">I can’t control you </span>but know that</p>
    <p class="line xl" style="--x:265px;--y:1144px">I’m here if you need me.</p>
  </div>
</div>
</body>
</html>
```